Bauzaunbanner für Fertigung und Montagen von Metallbau- und Stahlkonstruktionen
Zielgruppe
Fertigung und Montagen von Metallbau- und Stahlkonstruktionen
Aufgabenstellung
Außenwerbung an unserem Produktionsstandort (große halle); Blickdistanz ca. 50m; Stellengesuch 'Monteure' (w/m/d); Breite ca. 5.000mm; einfache (Bild-)Botschaft

```html
<!DOCTYPE html>
<html lang="de">
<head>
<meta charset="utf-8">
<title>Monteure gesucht – Bauzaunbanner</title>
<link rel="stylesheet" href="https://fonts.googleapis.com/css2?family=Montserrat:wght@500;600;700;800&display=swap">
<style>
  :root {
    --page-bg: #ebebeb;
    --brand-blue: #1170b8;
    --brand-navy: #0b4a7c;
    --white: #ffffff;
    --ink: #231f20;
  }
  * { margin: 0; padding: 0; box-sizing: border-box; }
  html, body {
    width: 1200px; height: 1200px; overflow: hidden;
    background: var(--page-bg);
    font-family: "Montserrat", Arial, sans-serif;
  }
  .banner {
    position: absolute;
    left: 225px; top: 510px;
    width: 750px; height: 180px;
    background: var(--brand-blue);
    box-shadow: 0 3px 6px rgba(0,0,0,0.25);
    overflow: hidden;
  }
  .banner-graphics {
    position: absolute; inset: 0;
    width: 100%; height: 100%;
  }
  .headline {
    position: absolute; left: 36px; top: 0;
    color: var(--white);
    font-weight: 800;
  }
  .headline-line {
    position: absolute; left: 0;
    white-space: nowrap;
    line-height: 1;
  }
  .headline-line.first {
    top: 9px;
    font-size: 39px;
  }
  .headline-line.second {
    top: 58px;
    font-size: 41px;
  }
  .headline .gender {
    font-weight: 500;
    font-size: 28px;
    margin-left: 4px;
  }
  .subline {
    position: absolute;
    left: 36px; top: 98px;
    color: var(--white);
    font-weight: 600;
    font-size: 25px;
    line-height: 1;
    white-space: nowrap;
  }
  .web-pill {
    position: absolute;
    left: 36px; top: 140px;
    width: 222px; height: 31px;
    border-radius: 16px;
    background: var(--white);
    color: var(--ink);
    font-weight: 700;
    font-size: 19.5px;
    line-height: 31px;
    text-align: center;
    white-space: nowrap;
  }
</style>
</head>
<body>
  <div class="banner">
    <svg class="banner-graphics" viewBox="0 0 750 180" preserveAspectRatio="none">
      <defs>
        <linearGradient id="photo-tones" x1="0" y1="0" x2="1" y2="1">
          <stop offset="0" stop-color="#f2f3f6"/>
          <stop offset="0.45" stop-color="#d9dde4"/>
          <stop offset="0.7" stop-color="#e87a2c"/>
          <stop offset="1" stop-color="#5a4a3a"/>
        </linearGradient>
      </defs>
      <polygon class="stripe-navy" points="426,0 476,0 362,180 310,180" fill="#0b4a7c"/>
      <polygon class="stripe-white" points="476,0 750,0 750,180 362,180" fill="#ffffff"/>
      <polygon class="stripe-blue" points="485,0 499,0 382,180 368,180" fill="#1170b8"/>
      <polygon class="photo-area" role="img"
        aria-label="Foto: Monteur mit Schutzhelm und Warnjacke verschraubt Trapezblech auf einem Dach"
        points="499,0 750,0 750,180 382,180" fill="url(#photo-tones)"/>
    </svg>
    <h1 class="headline">
      <span class="headline-line first">MONTEURE<span class="gender"> (m/w/d)</span></span>
      <span class="headline-line second">GESUCHT</span>
    </h1>
    <p class="subline">Metall- &amp; Stahlbau</p>
    <div class="web-pill">www.kessbach.de</div>
  </div>
</body>
</html>
```